Recruitment Flyer for Larkfield Lending company

Larkfield Lending centre requires a four page A4 color brochure for new staff who will be joining the organisation.

The brochure is received during the interview for the job role. so we are looking for nice glossy pictures combined with sufficient text to enable the applicant to make an informed decision.

I have attached a word document that may help plus lots of pictures that are on the website that could be used also.

Target Market(s)

New staff joining the organisation

Industry/Entity Type

Mortgage

Font styles to use
Sans Serif

Colors
3377b5
6b449b
b768aa
34a6d7

Requirements
Must have
• Glossy, colorful and career happy
Nice to have
• lots of photos and opportunity for text
Should not have
• be sad or not happy

```html
<!DOCTYPE html>
<html lang="en">
<head>
<meta charset="utf-8">
<title>Larkfield Lending – Staff Brochure</title>
<link rel="stylesheet" href="https://fonts.googleapis.com/css2?family=Marcellus&family=Open+Sans:wght@400;600;700&display=swap">
<style>
  :root{
    --cyan:#2fb8e8;
    --blue:#3377b5;
    --violet:#6b449b;
    --orchid:#b768aa;
    --ink:#333338;
    --body-text:#6a6a70;
    --mist:#e2e2e7;
    --night:#2a2b30;
    --stage-light:#ececec;
    --stage-mid:#e5e5e5;
    --stage-dark:#6e6e6e;
    --white:#ffffff;
  }
  *{margin:0;padding:0;box-sizing:border-box}
  html,body{width:1200px;height:3681px;overflow:hidden}
  body{position:relative;background:var(--stage-light);font-family:"Open Sans",Arial,sans-serif}
  .defs{position:absolute;width:0;height:0;overflow:hidden}

  .band{position:absolute;left:0;width:1200px}
  .band--cover{top:0;height:658px;background:var(--stage-light)}
  .band--outside{top:658px;height:642px;background:var(--stage-mid)}
  .band--inside{top:1300px;height:640px;background:var(--stage-light)}
  .band--flat{top:1940px;height:1741px;background:var(--stage-dark)}

  .page{display:block;background:var(--white);box-shadow:0 6px 18px rgba(0,0,0,.22)}
  .single{position:absolute;left:400px;top:46px;width:400px;height:566px}
  .spread{position:absolute;display:flex;box-shadow:0 8px 22px rgba(0,0,0,.25)}
  .spread .page{width:50%;height:100%;box-shadow:none}
  .spread::after{content:"";position:absolute;left:calc(50% - 14px);top:0;width:28px;height:100%;
    background:linear-gradient(90deg,rgba(0,0,0,0),rgba(0,0,0,.08) 50%,rgba(0,0,0,0));pointer-events:none}
  .spread--outside-small{left:200px;top:38px;width:800px;height:566px}
  .spread--inside-small{left:200px;top:37px;width:800px;height:566px}
  .spread--inside-large{left:58px;top:50px;width:1084px;height:766px}
  .spread--outside-large{left:58px;top:890px;width:1084px;height:766px}

  .fill-white{fill:var(--white)}
  .fill-cyan{fill:var(--cyan)}
  .fill-blue{fill:var(--blue)}
  .fill-violet{fill:var(--violet)}
  .fill-mist{fill:var(--mist)}
  .fill-ink{fill:var(--ink)}
  .rule-violet{stroke:var(--violet);stroke-width:.35;fill:none}
  .heading{font-family:"Marcellus",Georgia,serif}
  .wordmark{font-family:"Marcellus",Georgia,serif;letter-spacing:.3px}
  .tagline{font-family:"Open Sans",Arial,sans-serif;font-size:5px;letter-spacing:1.1px;fill:#55555a}
  .check-label{font-family:"Open Sans",Arial,sans-serif;font-weight:700;font-size:6px;fill:var(--ink)}
  .contact{font-family:"Open Sans",Arial,sans-serif;font-size:5px;fill:var(--white)}
  .step-num{font-family:"Open Sans",Arial,sans-serif;font-weight:700;font-size:5px;fill:var(--white)}
  .step-title{font-family:"Open Sans",Arial,sans-serif;font-weight:700;font-size:3.8px;fill:var(--violet)}
  .step-body{font-family:"Open Sans",Arial,sans-serif;font-size:3.2px;fill:var(--body-text)}
</style>
</head>
<body>

<svg class="defs" aria-hidden="true">
  <defs>
    <linearGradient id="photo-family" x1="0" y1="0" x2=".85" y2="1">
      <stop offset="0" stop-color="#4f8fd6"/>
      <stop offset=".16" stop-color="#9cc4ea"/>
      <stop offset=".3" stop-color="#b5523f"/>
      <stop offset=".42" stop-color="#e8c2a4"/>
      <stop offset=".55" stop-color="#c6b8e2"/>
      <stop offset=".66" stop-color="#f4d9c6"/>
      <stop offset=".8" stop-color="#6f9a3a"/>
      <stop offset="1" stop-color="#3f6b22"/>
    </linearGradient>
    <linearGradient id="photo-volunteers" x1="0" y1="0" x2="1" y2=".35">
      <stop offset="0" stop-color="#f0c7a8"/>
      <stop offset=".18" stop-color="#d9d9dc"/>
      <stop offset=".35" stop-color="#5f8a2e"/>
      <stop offset=".52" stop-color="#e6e6e8"/>
      <stop offset=".68" stop-color="#8ab04a"/>
      <stop offset=".84" stop-color="#f1cdb2"/>
      <stop offset="1" stop-color="#4c7322"/>
    </linearGradient>
    <linearGradient id="photo-moving" x1="0" y1="0" x2="1" y2=".4">
      <stop offset="0" stop-color="#f6eee4"/>
      <stop offset=".2" stop-color="#f1c9a8"/>
      <stop offset=".4" stop-color="#d7b38c"/>
      <stop offset=".58" stop-color="#e04848"/>
      <stop offset=".72" stop-color="#f7ddd0"/>
      <stop offset=".86" stop-color="#8a5a3c"/>
      <stop offset="1" stop-color="#fbf7f2"/>
    </linearGradient>
    <linearGradient id="faint-photo" x1="0" y1="0" x2="1" y2="0">
      <stop offset="0" stop-color="#ffffff"/>
      <stop offset="1" stop-color="#e8e8ee"/>
    </linearGradient>
    <radialGradient id="night-glow" cx=".5" cy=".35" r=".8">
      <stop offset="0" stop-color="#3a3b42"/>
      <stop offset="1" stop-color="#222327"/>
    </radialGradient>
    <g id="tick">
      <path d="M-1.4 0 L-.4 1.1 L1.5 -1.1" fill="none" stroke="#fff" stroke-width=".7" stroke-linecap="round" stroke-linejoin="round"/>
    </g>
  </defs>

  <symbol id="front-cover" viewBox="0 0 210 297">
    <rect width="210" height="297" class="fill-white"/>
    <polygon points="0,0 210,0 210,150 118,112 0,162" fill="url(#photo-family)" role="img" aria-label="Photo of a smiling family in front of their new home"/>
    <polygon points="0,162 118,112 210,150 210,168 118,130 0,180" class="fill-cyan"/>
    <polygon points="0,180 118,130 210,168 210,178 118,142 0,192" class="fill-mist"/>
    <polygon points="0,236 96,297 78,297 0,248" class="fill-mist"/>
    <polygon points="0,248 78,297 0,297" class="fill-violet"/>
    <circle cx="102" cy="224" r="5.5" class="fill-violet"/>
    <text x="111" y="227" font-size="8" class="wordmark fill-violet">LARKFIELD LENDING</text>
    <text x="200" y="251" font-size="14.5" text-anchor="end" class="heading fill-ink">HOME LOAN CENTER</text>
    <text x="200" y="261" text-anchor="end" class="tagline">LOREM DUMMY TEXT FOR PING</text>
    <g transform="translate(110 276)"><circle r="3" class="fill-blue"/><use href="#tick"/></g>
    <text x="115" y="278.2" class="check-label">LOREM</text>
    <g transform="translate(143 276)"><circle r="3" class="fill-blue"/><use href="#tick"/></g>
    <text x="148" y="278.2" class="check-label">LOREM</text>
    <g transform="translate(176 276)"><circle r="3" class="fill-blue"/><use href="#tick"/></g>
    <text x="181" y="278.2" class="check-label">LOREM</text>
  </symbol>

  <symbol id="back-cover" viewBox="0 0 210 297">
    <rect width="210" height="297" fill="url(#night-glow)"/>
    <circle cx="66" cy="98" r="6.5" class="fill-white"/>
    <text x="76" y="101.5" font-size="8.5" class="wordmark fill-white">LARKFIELD LENDING</text>
    <path d="M102 117 q3 -2.4 6 0 l-.8 1.6 h-4.4 z M101.6 119 h6.8 v2.2 h-6.8 z" class="fill-white"/>
    <text x="105" y="129" text-anchor="middle" class="contact">800 555 0184</text>
    <path d="M105 138 a2.4 2.4 0 0 1 2.4 2.4 c0 1.8 -2.4 4.4 -2.4 4.4 s-2.4 -2.6 -2.4 -4.4 a2.4 2.4 0 0 1 2.4 -2.4z" class="fill-white"/>
    <text x="105" y="152" text-anchor="middle" class="contact">2207 Harbour Lane Delta, BC V4K 2J8</text>
    <rect x="102" y="160" width="6" height="4" rx=".4" class="fill-white"/>
    <path d="M102 160.3 l3 2 l3 -2" fill="none" stroke="#2a2b30" stroke-width=".4"/>
    <text x="105" y="172" text-anchor="middle" class="contact">info@larkfieldlending.com</text>
    <polygon points="0,297 0,262 118,218 210,256 210,297" class="fill-white"/>
    <polygon points="0,246 118,198 118,214 0,262" class="fill-violet"/>
    <polygon points="118,198 210,236 210,252 118,214" class="fill-mist"/>
  </symbol>

  <symbol id="inside-left" viewBox="0 0 210 297">
    <rect width="210" height="297" class="fill-white"/>
    <polygon points="0,0 210,0 210,48 0,104" fill="url(#photo-volunteers)" role="img" aria-label="Photo of smiling community volunteers outdoors"/>
    <polygon points="0,104 210,48 210,62 0,118" class="fill-cyan"/>
    <polygon points="0,118 210,62 210,150 0,150" fill="url(#faint-photo)" role="img" aria-label="Faint photo of stacked coins"/>
    <g transform="translate(0 160)">
      <circle cx="64" cy="0" r="4.5" class="fill-violet"/><text x="64" y="1.8" text-anchor="middle" class="step-num">1</text>
      <text x="76" y="-1.5" class="step-title">STORY</text>
      <text class="step-body"><tspan x="76" y="2.6">is simply dummy text of the printing and typesetting industry.</tspan><tspan x="76" y="6.4">Lorem Ipsum has been the industry's standard dummy text ever</tspan><tspan x="76" y="10.2">since the 1500s, when an unknown printer took a galley of type and</tspan><tspan x="76" y="14">scrambled it to make a type specimen book.</tspan></text>
    </g>
    <g transform="translate(0 190)">
      <circle cx="64" cy="0" r="4.5" class="fill-violet"/><text x="64" y="1.8" text-anchor="middle" class="step-num">2</text>
      <text x="76" y="-1.5" class="step-title">STORY</text>
      <text class="step-body"><tspan x="76" y="2.6">is simply dummy text of the printing and typesetting industry.</tspan><tspan x="76" y="6.4">Lorem Ipsum has been the industry's standard dummy text ever</tspan><tspan x="76" y="10.2">since the 1500s, when an unknown printer</tspan></text>
    </g>
    <g transform="translate(0 220)">
      <circle cx="64" cy="0" r="4.5" class="fill-violet"/><text x="64" y="1.8" text-anchor="middle" class="step-num">3</text>
      <text x="76" y="-1.5" class="step-title">STORY</text>
      <text class="step-body"><tspan x="76" y="2.6">is simply dummy text of the printing and typesetting industry.</tspan><tspan x="76" y="6.4">Lorem Ipsum has been the industry's standard dummy text ever</tspan><tspan x="76" y="10.2">since the 1500s, when an unknown printer took a galley of type and</tspan><tspan x="76" y="14">scrambled it to make a type specimen book.</tspan></text>
    </g>
    <g transform="translate(0 250)">
      <circle cx="64" cy="0" r="4.5" class="fill-violet"/><text x="64" y="1.8" text-anchor="middle" class="step-num">4</text>
      <text x="76" y="-1.5" class="step-title">STORY</text>
      <text class="step-body"><tspan x="76" y="2.6">is simply dummy text of the printing and typesetting industry.</tspan><tspan x="76" y="6.4">Lorem Ipsum has been the industry's standard dummy text ever</tspan><tspan x="76" y="10.2">since the 1500s, when an unknown printer took a galley of type and</tspan><tspan x="76" y="14">scrambled it to make a type specimen book.</tspan></text>
    </g>
    <circle cx="13" cy="285" r="2.6" class="fill-violet"/>
    <text x="17.5" y="286.6" font-size="4.4" class="wordmark fill-violet">LARKFIELD LENDING</text>
    <line x1="66" y1="286" x2="210" y2="286" class="rule-violet"/>
  </symbol>

  <symbol id="inside-right" viewBox="0 0 210 297">
    <rect width="210" height="297" class="fill-white"/>
    <polygon points="0,0 210,0 210,95 0,48" fill="url(#photo-moving)" role="img" aria-label="Photo of a happy family unpacking moving boxes"/>
    <polygon points="0,48 210,95 210,109 0,62" class="fill-cyan"/>
    <polygon points="150,122 210,106 210,138" class="fill-violet"/>
    <polygon points="60,230 210,210 210,280 60,280" fill="url(#faint-photo)" role="img" aria-label="Faint photo of a model house in open hands"/>
    <g transform="translate(0 160)">
      <circle cx="18" cy="0" r="4.5" class="fill-violet"/><text x="18" y="1.8" text-anchor="middle" class="step-num">5</text>
      <text x="30" y="-1.5" class="step-title">STORY</text>
      <text class="step-body"><tspan x="30" y="2.6">is simply dummy text of the printing and typesetting industry.</tspan><tspan x="30" y="6.4">Lorem Ipsum has been the industry's standard dummy text ever</tspan><tspan x="30" y="10.2">since the 1500s, when an unknown printer took a galley of type and</tspan><tspan x="30" y="14">scrambled it to make a type specimen book.</tspan></text>
    </g>
    <g transform="translate(0 190)">
      <circle cx="18" cy="0" r="4.5" class="fill-violet"/><text x="18" y="1.8" text-anchor="middle" class="step-num">6</text>
      <text x="30" y="-1.5" class="step-title">STORY</text>
      <text class="step-body"><tspan x="30" y="2.6">is simply dummy text of the printing and typesetting industry.</tspan><tspan x="30" y="6.4">Lorem Ipsum has been the industry's standard dummy text ever</tspan><tspan x="30" y="10.2">since the 1500s, when an unknown printer took a galley of type and</tspan><tspan x="30" y="14">scrambled it to make a type specimen book.</tspan></text>
    </g>
    <g transform="translate(0 220)">
      <circle cx="18" cy="0" r="4.5" class="fill-violet"/><text x="18" y="1.8" text-anchor="middle" class="step-num">7</text>
      <text x="30" y="-1.5" class="step-title">STORY</text>
      <text class="step-body"><tspan x="30" y="2.6">is simply dummy text of the printing and typesetting industry.</tspan><tspan x="30" y="6.4">Lorem Ipsum has been the industry's standard dummy text ever</tspan><tspan x="30" y="10.2">since the 1500s, when an unknown printer took a galley of type and</tspan><tspan x="30" y="14">scrambled it to make a type specimen book.</tspan></text>
    </g>
    <g transform="translate(0 250)">
      <circle cx="18" cy="0" r="4.5" class="fill-violet"/><text x="18" y="1.8" text-anchor="middle" class="step-num">8</text>
      <text x="30" y="-1.5" class="step-title">STORY</text>
      <text class="step-body"><tspan x="30" y="2.6">is simply dummy text of the printing and typesetting industry.</tspan><tspan x="30" y="6.4">Lorem Ipsum has been the industry's standard dummy text ever</tspan><tspan x="30" y="10.2">since the 1500s, when an unknown printer took a galley of type and</tspan><tspan x="30" y="14">scrambled it to make a type specimen book.</tspan></text>
    </g>
    <line x1="0" y1="286" x2="146" y2="286" class="rule-violet"/>
    <circle cx="151" cy="285" r="2.6" class="fill-violet"/>
    <text x="155.5" y="286.6" font-size="4.4" class="wordmark fill-violet">LARKFIELD LENDING</text>
  </symbol>
</svg>

<section class="band band--cover">
  <svg class="page single" viewBox="0 0 210 297"><use href="#front-cover"/></svg>
</section>

<section class="band band--outside">
  <div class="spread spread--outside-small">
    <svg class="page" viewBox="0 0 210 297"><use href="#back-cover"/></svg>
    <svg class="page" viewBox="0 0 210 297"><use href="#front-cover"/></svg>
  </div>
</section>

<section class="band band--inside">
  <div class="spread spread--inside-small">
    <svg class="page" viewBox="0 0 210 297"><use href="#inside-left"/></svg>
    <svg class="page" viewBox="0 0 210 297"><use href="#inside-right"/></svg>
  </div>
</section>

<section class="band band--flat">
  <div class="spread spread--inside-large">
    <svg class="page" viewBox="0 0 210 297"><use href="#inside-left"/></svg>
    <svg class="page" viewBox="0 0 210 297"><use href="#inside-right"/></svg>
  </div>
  <div class="spread spread--outside-large">
    <svg class="page" viewBox="0 0 210 297"><use href="#back-cover"/></svg>
    <svg class="page" viewBox="0 0 210 297"><use href="#front-cover"/></svg>
  </div>
</section>

</body>
</html>
```